Needed Box Packaging: Dog XL Puppy Pee/Poo Pads

We're looking for a creative and fun design for our XL puppy pads. Attached is all the documents you will need.

Our pads are unique with Bamboo Charcoal and optional Adhesive sticker backing on the corners. 23" x 35" is the size. There's 50 per box.

ABSORBS 2x as much, 2x as fast, so you never come home to ruined floors
BLACK puppy pads, so your pets mess stays discrete and you never see a yellow stain on a white puppy pad in your home
ODOR ELIMINATION with carbon technology for all-day use to ensure your home stays fresh
LEAK PROOF Tidewell Polymer turns liquid into gel instantly to guarantee dry floors and easy clean up
PHEROMONE ATTRACTION to ensure pets feel comfortable and knows to hit the right spot every time

Target Market(s)

Dog owners

Font styles to use
Sans Serif

Colors
33a6d7
33b8a4
acd036
fbee3d
faa54b

Requirements
Must have
• Must have logo, size of pads, benefits, UPC code, number packed per box, pictures of a dog and picture of the pads
Should not have
• cats

```html
<!DOCTYPE html>
<html lang="en">
<head>
<meta charset="utf-8">
<title>XL Puppy Pads – Box Front</title>
<link href="https://fonts.googleapis.com/css2?family=Oswald:wght@500;700&family=Roboto+Condensed:wght@400;700&display=swap" rel="stylesheet">
<style>
  :root {
    --stage: #eeeeee;
    --navy: #1d3f86;
    --blue: #33a6d7;
    --blue-deep: #2a62b8;
    --sky: #d9f1fb;
    --sky-mid: #b6e3f5;
    --green: #5cc21a;
    --grass-dark: #2f6a1c;
    --grass: #5e9d35;
    --grass-light: #9cc95a;
    --gold: #faa54b;
    --yellow: #fbee3d;
    --white: #ffffff;
    --silver: #e4e8ee;
  }
  * { box-sizing: border-box; margin: 0; padding: 0; }
  html, body { width: 1200px; height: 996px; overflow: hidden; background: var(--stage); }
  body { font-family: "Roboto Condensed", Arial, sans-serif; }

  .box-front {
    position: absolute; left: 50px; top: 118px;
    width: 1100px; height: 760px; overflow: hidden;
  }
  .photo-dog-on-grass {
    position: absolute; inset: 0;
    background:
      radial-gradient(ellipse 260px 240px at 300px 480px, #f4f4f2 0%, #e8e8e4 60%, rgba(232,232,228,0) 100%),
      linear-gradient(180deg, var(--grass-dark) 0%, var(--grass) 45%, var(--grass-light) 85%, var(--grass) 100%);
  }
  .info-panel { position: absolute; inset: 0; }

  .brand-mark {
    position: absolute; left: 36px; top: 112px;
    display: flex; align-items: center; gap: 10px;
  }
  .brand-mark .dot { width: 26px; height: 26px; border-radius: 50%; background: var(--white); }
  .brand-mark .name {
    font-family: "Oswald", sans-serif; font-weight: 700; font-size: 30px;
    color: var(--white); letter-spacing: 1px;
  }

  .product-title {
    position: absolute; left: 210px; top: 96px; width: 380px; height: 130px;
    border-radius: 0 65px 65px 0;
    background: linear-gradient(180deg, #4f8fd6 0%, var(--blue-deep) 60%, var(--navy) 100%);
    display: flex; align-items: center; padding-left: 24px; gap: 14px;
    box-shadow: 0 6px 14px rgba(0,0,0,.3);
  }
  .product-title .size {
    font-family: "Oswald", sans-serif; font-weight: 700; font-size: 112px; line-height: 1;
    color: var(--silver); letter-spacing: -4px;
  }
  .product-title .kind {
    font-family: "Oswald", sans-serif; font-weight: 700; font-size: 46px; line-height: .95;
    color: var(--yellow);
  }

  .benefits { position: absolute; left: 600px; top: 50px; width: 470px; color: var(--navy); }
  .benefits h2 {
    font-family: "Oswald", sans-serif; font-weight: 500; font-size: 40px; line-height: 1;
  }
  .benefits .lead { font-size: 12px; font-weight: 700; text-transform: uppercase; margin: 4px 0 14px; }
  .benefit { display: flex; gap: 10px; margin-bottom: 12px; }
  .benefit svg { flex: 0 0 24px; margin-top: 4px; }
  .benefit h3 {
    font-family: "Oswald", sans-serif; font-weight: 500; font-size: 23px; line-height: 1.02;
    color: var(--green); text-transform: uppercase;
  }
  .benefit p { font-size: 11px; font-weight: 700; text-transform: uppercase; line-height: 1.2; }

  .layer-labels { position: absolute; left: 430px; top: 430px; width: 240px; }
  .layer {
    display: flex; align-items: center; gap: 6px; height: 38px; margin-bottom: 6px;
    padding: 0 28px 0 10px; color: var(--white);
    clip-path: polygon(0 0, 100% 0, 88% 100%, 0 100%);
  }
  .layer strong { font-family: "Oswald", sans-serif; font-weight: 500; font-size: 19px; white-space: nowrap; }
  .layer small { font-size: 8px; font-weight: 700; text-transform: uppercase; line-height: 1.1; }
  .layer.light { background: #6cc0e6; color: var(--navy); }
  .layer.mid { background: #3b7fcc; }
  .layer.dark { background: var(--navy); }
  .layer.feature { height: 78px; flex-direction: column; align-items: flex-start; justify-content: center; background: #4f9be8; gap: 2px; }

  .pad-layers-illustration {
    position: absolute; left: 700px; top: 440px; width: 380px; height: 260px;
    border-radius: 50%;
    background: radial-gradient(ellipse at center, #ffffff 0%, #cfe9f6 45%, rgba(207,233,246,0) 75%),
                linear-gradient(180deg, #d8dde2 0%, #9aa3ac 100%);
  }
  .layers-caption {
    position: absolute; left: 830px; top: 545px; text-align: center;
    font-family: "Oswald", sans-serif; font-weight: 700; color: var(--gold);
    text-shadow: 0 2px 0 #8a5a12; transform: rotate(-6deg); line-height: .95;
  }
  .layers-caption .big { font-size: 48px; }
  .layers-caption .small { font-size: 30px; }

  .pack-count {
    position: absolute; left: 30px; top: 598px; width: 340px; height: 120px;
    border-radius: 60px 0 0 60px;
    background: linear-gradient(180deg, var(--yellow) 0%, var(--gold) 100%);
    display: flex; align-items: center; padding-left: 24px; gap: 10px;
    clip-path: polygon(0 0, 100% 0, 90% 100%, 0 100%);
  }
  .pack-count .qty {
    font-family: "Oswald", sans-serif; font-weight: 700; font-size: 100px; line-height: 1;
    color: var(--silver); text-shadow: 0 3px 0 #7d7d7d;
  }
  .pack-count .unit { font-family: "Oswald", sans-serif; font-weight: 700; line-height: 1; }
  .pack-count .unit .word { font-size: 44px; color: var(--silver); text-shadow: 0 2px 0 #7d7d7d; display: block; }
  .pack-count .unit .dims { font-size: 26px; color: var(--navy); }
</style>
</head>
<body>
  <main class="box-front">
    <div class="photo-dog-on-grass" role="img" aria-label="Photo of a small white fluffy puppy sitting on green grass"></div>

    <svg class="info-panel" width="1100" height="760" viewBox="0 0 1100 760" aria-hidden="true">
      <defs>
        <linearGradient id="panelFill" x1="0" y1="0" x2="0" y2="1">
          <stop offset="0" stop-color="#d9f1fb"/>
          <stop offset=".7" stop-color="#b6e3f5"/>
          <stop offset="1" stop-color="#b6e3f5" stop-opacity="0"/>
        </linearGradient>
      </defs>
      <path d="M430,0 Q520,180 555,430 Q580,600 640,760 L1100,760 L1100,0 Z" fill="url(#panelFill)"/>
      <path d="M430,0 Q520,180 555,430 Q580,600 640,760" fill="none" stroke="#33a6d7" stroke-width="14" opacity=".7"/>
    </svg>

    <div class="brand-mark"><span class="dot"></span><span class="name">Pawlane</span></div>

    <div class="product-title">
      <span class="size">XL</span>
      <span class="kind">PUPPY<br>PADS</span>
    </div>

    <section class="benefits">
      <h2>WITH BAMBOO CHARCOAL</h2>
      <p class="lead">and optional adhesive sticker backing on the corners</p>

      <div class="benefit">
        <svg width="24" height="22" viewBox="0 0 24 22"><path d="M2,12 L9,19 L22,2" fill="none" stroke="#33a6d7" stroke-width="4"/></svg>
        <div><h3>Absorbs 2x as much, 2x as fast</h3><p>so you never come home to ruined floors</p></div>
      </div>
      <div class="benefit">
        <svg width="24" height="22" viewBox="0 0 24 22"><path d="M2,12 L9,19 L22,2" fill="none" stroke="#33a6d7" stroke-width="4"/></svg>
        <div><h3>Black puppy pads</h3><p>so your pets mess stays discrete and you never see a<br>yellow stain on a white puppy pad in your home</p></div>
      </div>
      <div class="benefit">
        <svg width="24" height="22" viewBox="0 0 24 22"><path d="M2,12 L9,19 L22,2" fill="none" stroke="#33a6d7" stroke-width="4"/></svg>
        <div><h3>Odor elimination with<br>carbon technology</h3><p>for all-day use to ensure your home stays fresh</p></div>
      </div>
      <div class="benefit">
        <svg width="24" height="22" viewBox="0 0 24 22"><path d="M2,12 L9,19 L22,2" fill="none" stroke="#33a6d7" stroke-width="4"/></svg>
        <div><h3>Leak proof Tidewell Polymer</h3><p>turns liquid into gel instantly to guarantee<br>dry floors and easy clean up</p></div>
      </div>
      <div class="benefit">
        <svg width="24" height="22" viewBox="0 0 24 22"><path d="M2,12 L9,19 L22,2" fill="none" stroke="#33a6d7" stroke-width="4"/></svg>
        <div><h3>Pheromone attraction</h3><p>to ensure pets feel comfortable and knows to hit the<br>right spot every time</p></div>
      </div>
    </section>

    <div class="layer-labels">
      <div class="layer light"><strong>TEAR RESISTANT</strong><small>top<br>sheet</small></div>
      <div class="layer mid"><strong>QUILTED</strong><small>draws in moisture to<br>prevent tracking</small></div>
      <div class="layer dark"><strong>QUILTED</strong><small>draws in moisture to<br>prevent tracking</small></div>
      <div class="layer feature"><strong>QUICK DRYING GEL</strong><small>provides immediate absorption, converts<br>liquid to gel and locks in moisture</small></div>
      <div class="layer dark"><strong>QUILTED</strong><small>draws in moisture to<br>prevent tracking</small></div>
      <div class="layer dark"><strong>LEAK-PROOF</strong><small>plastic liner</small></div>
    </div>

    <div class="pad-layers-illustration" role="img" aria-label="Exploded view of the six stacked pad layers"></div>
    <div class="layers-caption"><span class="big">6 LAYERS</span><br><span class="small">COMPOSITION</span></div>

    <div class="pack-count">
      <span class="qty">50</span>
      <span class="unit"><span class="word">PADS</span><span class="dims">23" x 35"</span></span>
    </div>
  </main>
</body>
</html>
```